Kitchen Tools Infographic - Helpful Items for Healthy Home Meals

We are a weight loss company that provides holistic, natural nutrition programs to consumers -- you can see our web site at www.FernaluVita.com. We need a simple infographic to be shared on social media and via email. The topic for the infographic is "Equip Your Kitchen for Healthy Home Meals". We've outlined 5 groups of kitchen tools that are helpful for consumers to have for preparing home meals, and included some framing statistics emphasizing the weight management benefits of preparing meals versus eating out.

Target Market(s)

Women age 35-55

Industry/Entity Type

Health And Wellness

Font styles to use
Sans Serif

Colors
0292cd
9bcb3b

Requirements
Must have
• - FernaluVita Logo
• - Graphics summarizing statistic (weight gain)
• - Graphics showing groupings of kitchen tools
Should not have
• body scale graphics
• before/after graphics

```html
<!DOCTYPE html>
<html lang="en">
<head>
<meta charset="utf-8">
<title>Equip Your Kitchen for Healthy Home Meals – FernaluVita</title>
<link href="https://fonts.googleapis.com/css2?family=Bebas+Neue&family=Fira+Sans:wght@400;500;600&family=Fira+Sans+Condensed:wght@400;500&family=Open+Sans:wght@400;700&display=swap" rel="stylesheet">
<style>
  :root{
    --stage:#a29e95;
    --blue:#0292cd;
    --blue-deep:#0a6fae;
    --blue-light:#5ec8f2;
    --green:#9bcb3b;
    --green-mid:#7aa63a;
    --green-dark:#5f6e34;
    --yellow:#f5e43a;
    --cream:#f3ead2;
    --orange:#e8632a;
    --brown:#8a5a3a;
    --brown-dark:#7a4d31;
    --brown-side:#6f4630;
    --ink:#222;
    --white:#fff;
  }
  html,body{margin:0;padding:0;width:1200px;height:1200px;overflow:hidden;background:var(--stage);}
  .poster{position:absolute;left:305px;top:18px;width:590px;height:1164px;overflow:hidden;font-family:"Open Sans",sans-serif;}
  section{position:absolute;left:0;width:590px;}

  /* intro */
  .intro{top:0;height:276px;background:linear-gradient(to bottom,var(--cream) 0%,#efe3c4 86%,#b9c97a 93%,#9bb85a 100%);}
  .food-left{position:absolute;left:0;top:0;width:120px;height:230px;border-radius:0 0 60px 0;background:linear-gradient(160deg,#e7e2d9,#d9954c 55%,#f0cc5a);opacity:.85;}
  .food-right{position:absolute;right:0;top:0;width:72px;height:200px;border-radius:0 0 0 50px;background:linear-gradient(180deg,#c0403a,#6fae3c 55%,#e05a2c);opacity:.85;}
  .apron{position:absolute;left:22px;top:36px;width:150px;height:256px;background:var(--green-mid);border-radius:30px 30px 14px 14px;z-index:3;}
  .apron-text{position:absolute;left:0;top:114px;width:150px;text-align:center;font-family:"Fira Sans",sans-serif;font-weight:600;font-size:33px;line-height:32px;color:#f6ee9a;}
  .ribbon{position:absolute;left:157px;top:0;width:344px;height:53px;background:var(--blue);border-radius:0 0 28px 28px;display:flex;align-items:center;justify-content:center;font-family:"Bebas Neue",sans-serif;font-size:38px;letter-spacing:9px;color:var(--white);}
  .headline{position:absolute;left:180px;top:74px;width:318px;margin:0;text-align:center;font-family:"Fira Sans",sans-serif;font-weight:500;font-size:27px;line-height:33px;color:var(--orange);}
  .divider{position:absolute;top:168px;height:1.5px;background:var(--green);}
  .divider.l{left:200px;width:88px}.divider.r{left:392px;width:100px}
  .lead{position:absolute;left:172px;top:196px;width:340px;margin:0;text-align:center;font-size:11.6px;line-height:17px;color:var(--ink);}

  /* charts */
  .chart{color:var(--white);}
  .chart svg{display:block}
  .calories{top:276px;height:141px;background:var(--brown);}
  .gain{top:417px;height:174px;background:var(--brown-dark);}
  .chart-title{font-family:"Fira Sans Condensed",sans-serif;font-weight:500;font-size:20px;fill:var(--yellow);}
  .chart-label{font-family:"Fira Sans Condensed",sans-serif;font-size:14px;fill:var(--white);}
  .axis{font-family:"Open Sans",sans-serif;font-size:9.5px;fill:var(--white);}

  /* tools */
  .tools{top:591px;height:446px;background:var(--blue);}
  .tools-slogan{position:absolute;left:0;top:0;width:164px;height:446px;background:var(--blue-deep);}
  .slogan-rule{position:absolute;left:18px;width:128px;height:3px;background:var(--blue-light);}
  .slogan{position:absolute;left:14px;top:28px;width:140px;font-family:"Bebas Neue",sans-serif;text-align:center;line-height:.94;margin:0;}
  .slogan span{display:block}
  .s-make{font-size:74px;color:var(--white)}
  .s-healthy{font-size:46px;color:var(--yellow)}
  .s-eating{font-size:62px;color:var(--blue-light)}
  .s-easier{font-size:56px;color:var(--white);letter-spacing:2px}
  .s-with{font-size:37px;color:var(--white)}
  .s-kitchen{font-size:52px;color:var(--blue-light)}
  .s-tools{font-size:72px;color:var(--yellow)}
  .group{position:absolute;left:180px;width:400px;color:var(--white);}
  .group-head{display:flex;align-items:center;gap:12px;height:30px;}
  .group-title{margin:0;font-family:"Fira Sans",sans-serif;font-weight:500;font-size:25px;color:#fff6a8;}
  .group ul{list-style:none;margin:1px 0 0 -3px;padding:0;font-size:9.2px;line-height:13.5px;}
  .group b{font-weight:700}

  /* footer */
  .invite{top:1037px;height:72px;background:var(--green-mid);text-align:center;color:var(--white);font-family:"Fira Sans",sans-serif;}
  .invite p{margin:10px 0 0;font-size:15px;line-height:17px;font-weight:500}
  .contact{display:inline-block;margin-top:6px;padding:1px 12px;border:1.5px solid var(--white);border-radius:14px;font-size:14px;font-weight:500;}
  .brand{top:1109px;height:55px;background:var(--green-dark);text-align:center;font-family:"Fira Sans",sans-serif;}
  .brand-name{margin:5px 0 0;font-size:22px;font-weight:500;color:#bfe3f5;}
  .brand-url{margin:0;font-size:14px;font-weight:600;color:var(--white);}
</style>
</head>
<body>
<main class="poster">

  <section class="intro">
    <div class="food-left" role="img" aria-label="Illustration of rice bowl, bread and cheese"></div>
    <div class="food-right" role="img" aria-label="Illustration of meat, shrimp, lettuce, tomatoes and carrots"></div>
    <div class="ribbon">Infographic</div>
    <h1 class="headline">Equip Your Kitchen for Healthy Home Meals</h1>
    <div class="divider l"></div><div class="divider r"></div>
    <p class="lead">Those who eat out consume an average of 134 calories more per meal. Americans eat out an average of 4.5 times per week, so those extra calories can add up to substantial weight gain -- and give you a reason to prepare your own meals.</p>
    <div class="apron" role="img" aria-label="Green kitchen apron illustration">
      <div class="apron-text">WHY<br>COOK<br>AT<br>HOME?</div>
    </div>
  </section>

  <section class="chart calories">
    <svg width="590" height="141" viewBox="0 0 590 141">
      <rect x="505" y="0" width="85" height="141" fill="var(--brown-side)"/>
      <text class="chart-title" x="270" y="43" text-anchor="middle">EXCESS CALORIES FROM RESTAURANT MEALS</text>
      <g stroke="#a27452" stroke-width="1">
        <line x1="169" y1="52" x2="169" y2="115"/><line x1="214" y1="52" x2="214" y2="115"/>
        <line x1="260" y1="52" x2="260" y2="115"/><line x1="305" y1="52" x2="305" y2="115"/>
        <line x1="350" y1="52" x2="350" y2="115"/><line x1="396" y1="52" x2="396" y2="115"/>
        <line x1="441" y1="52" x2="441" y2="115"/><line x1="486" y1="52" x2="486" y2="115"/>
      </g>
      <defs><linearGradient id="barBlue" x1="0" x2="1"><stop offset="0" stop-color="#0292cd"/><stop offset="1" stop-color="#8fd8f6"/></linearGradient></defs>
      <rect x="169" y="58" width="272" height="16" fill="url(#barBlue)"/>
      <rect x="169" y="86" width="72" height="15" fill="url(#barBlue)"/>
      <text class="chart-label" x="160" y="71" text-anchor="end">Calories Per Week</text>
      <text class="chart-label" x="160" y="99" text-anchor="end">Calories Per Meal</text>
      <g class="axis" text-anchor="middle">
        <text x="169" y="130">0</text><text x="214" y="130">100</text><text x="260" y="130">200</text>
        <text x="305" y="130">300</text><text x="350" y="130">400</text><text x="396" y="130">500</text>
        <text x="441" y="130">600</text><text x="486" y="130">700</text>
      </g>
      <g role="img" aria-label="Calorie dial icon">
        <circle cx="556" cy="70" r="47" fill="var(--white)" stroke="var(--green)" stroke-width="3"/>
      </g>
    </svg>
  </section>

  <section class="chart gain">
    <svg width="590" height="174" viewBox="0 0 590 174">
      <rect x="505" y="0" width="85" height="174" fill="var(--brown-side)"/>
      <text class="chart-title" x="270" y="30" text-anchor="middle">POUNDS GAIN FROM RESTAURANT MEALS</text>
      <g stroke="#b08463" stroke-width="1">
        <line x1="67" y1="47" x2="475" y2="47"/><line x1="67" y1="68" x2="475" y2="68"/>
        <line x1="67" y1="89" x2="475" y2="89"/><line x1="67" y1="110" x2="475" y2="110"/>
        <line x1="67" y1="131" x2="475" y2="131"/><line x1="67" y1="152" x2="475" y2="152"/>
      </g>
      <g class="axis" text-anchor="end">
        <text x="60" y="51">10</text><text x="60" y="72">8</text><text x="60" y="93">6</text>
        <text x="60" y="114">4</text><text x="60" y="135">2</text><text x="60" y="156">0</text>
      </g>
      <g fill="var(--green-mid)">
        <rect x="103" y="133" width="22" height="19"/>
        <rect x="240" y="107" width="22" height="45"/>
        <rect x="386" y="57" width="22" height="95"/>
      </g>
      <g class="axis" text-anchor="middle">
        <text x="114" y="170">2 Months</text><text x="251" y="170">6 Months</text><text x="397" y="170">1 Year</text>
      </g>
      <g role="img" aria-label="Round icon">
        <circle cx="556" cy="90" r="47" fill="var(--white)" stroke="var(--blue)" stroke-width="3"/>
      </g>
    </svg>
  </section>

  <section class="tools">
    <div class="tools-slogan">
      <div class="slogan-rule" style="top:18px"></div>
      <h2 class="slogan">
        <span class="s-make">MAKE</span>
        <span class="s-healthy">HEALTHY</span>
        <span class="s-eating">EATING</span>
        <span class="s-easier">EASIER</span>
        <span class="s-with">WITH THESE</span>
        <span class="s-kitchen">KITCHEN</span>
        <span class="s-tools">TOOLS</span>
      </h2>
      <div class="slogan-rule" style="top:421px"></div>
    </div>

    <div class="group" style="top:17px">
      <div class="group-head"><h3 class="group-title">1. PREP</h3>
        <svg width="110" height="34" viewBox="0 0 110 34" fill="none" stroke="#fff" stroke-width="2"><rect x="4" y="3" width="18" height="28" rx="2"/><path d="M40 2v20M40 22v10" stroke-width="4"/><rect x="62" y="16" width="44" height="14" rx="3"/><path d="M68 16c2-8 30-8 32 0"/></svg>
      </div>
      <ul>
        <li><b>Cutting Board</b> – essential for prepping meat and vegetables</li>
        <li><b>Chef’s Knife</b> – go for quality to make chopping, dicing and slicing faster and easier</li>
        <li><b>Digital Food Scale</b> – get the precision you need for perfect recipes and portion control</li>
      </ul>
    </div>

    <div class="group" style="top:103px">
      <div class="group-head"><h3 class="group-title">2. TECH</h3>
        <svg width="140" height="34" viewBox="0 0 140 34" fill="#fff"><rect x="4" y="2" width="14" height="22" rx="2"/><rect x="2" y="24" width="18" height="8"/><rect x="26" y="12" width="36" height="20" rx="3"/><rect x="38" y="6" width="12" height="5"/><rect x="72" y="10" width="34" height="22" rx="2"/><rect x="106" y="18" width="30" height="4"/></svg>
      </div>
      <ul>
        <li><b>High-Powered Blender</b> - make highly nutritious, healthy drinks from fruits and veggies</li>
        <li><b>Slow Cooker</b> - cook delicious meals while you are at work</li>
        <li><b>Pressure Cooker</b> - create single pot meals in 20 minutes or</li>
      </ul>
    </div>

    <div class="group" style="top:192px">
      <div class="group-head"><h3 class="group-title">3. COOK</h3>
        <svg width="150" height="34" viewBox="0 0 150 34"><rect x="4" y="6" width="26" height="24" rx="3" fill="#fff"/><path d="M36 26h34l-4 5H40z" fill="#fff"/><rect x="70" y="26" width="22" height="3" fill="#fff"/><rect x="106" y="6" width="36" height="22" rx="3" fill="none" stroke="#fff" stroke-width="2"/></svg>
      </div>
      <ul>
        <li><b>Ceramic Pan</b> - nonstick cooking surface allows you to cook without oil</li>
        <li><b>Vegetable Steamer</b> - preserve nutrients and natural, fresh taste</li>
        <li><b>Baking Sheet</b> - ideal for roasting vegetables in the oven or baking chicken and fish dishes</li>
      </ul>
    </div>

    <div class="group" style="top:272px">
      <div class="group-head"><h3 class="group-title">4. SERVE</h3>
        <svg width="130" height="34" viewBox="0 0 130 34" fill="#fff"><path d="M4 8h26l-4 7H8zM4 18h26l-4 7H8z"/><path d="M48 30L76 4v26z"/><circle cx="106" cy="17" r="12" fill="none" stroke="#fff" stroke-width="3"/></svg>
      </div>
      <ul>
        <li><b>Cloth Napkins</b> - to reduce waste and dress up your table</li>
        <li><b>Dinnerware</b> - pre-plate meals rather than serving family style to control portions</li>
        <li><b>Small Plates</b> - use salad plates and smaller dishware to manage perception of food volume</li>
      </ul>
    </div>

    <div class="group" style="top:360px">
      <div class="group-head"><h3 class="group-title">5. STORE</h3>
        <svg width="150" height="34" viewBox="0 0 150 34" fill="none" stroke="#fff" stroke-width="2.5"><rect x="4" y="8" width="42" height="20" rx="6"/><rect x="74" y="6" width="18" height="26" rx="3"/><rect x="112" y="2" width="24" height="30"/></svg>
      </div>
      <ul>
        <li><b>Glass Storage Containers</b> - keep your healthy leftovers so nothing goes to waste</li>
        <li><b>Mason Jars</b> - perfect for premade salads that you can bring to work</li>
        <li><b>Freezer Safe Re-Sealable Bags</b> - prepare double batches to make the most of your time</li>
      </ul>
    </div>
  </section>

  <section class="invite">
    <p>FernaluVita can help you develop healthier eating habits.<br>We invite you to learn more.</p>
    <span class="contact">CONTACT US »</span>
  </section>

  <section class="brand">
    <p class="brand-name">FernaluVita</p>
    <p class="brand-url">www.fernaluvita.com</p>
  </section>

</main>
</body>
</html>
```